Lumo Brew Premium Matcha brand Label

This is a label design project for a luxury tea brand. Feel free to be creative within the guidelines.
Attached to this project is a document called “Private Label Design Requirements” with the design guidelines and template. There is another document called "Lumo Brew Packaging Instructions" this has more details necessary to stick to the guidelines in the first document.

I have also attached the certifications to be included as well as different variations of the logo for you to use.

If you have any questions, I am here.
Updates

Target Market(s)

Young, active, fun, enjoy the finer things

```html
<!DOCTYPE html>
<html lang="en">
<head>
<meta charset="utf-8">
<title>Lumo Brew Premium Matcha Label</title>
<link rel="stylesheet" href="https://fonts.googleapis.com/css2?family=Fredoka:wght@400;500;600;700&family=Alfa+Slab+One&display=swap">
<style>
  :root {
    --paper: #ffffff;
    --pattern-light: #eef4ea;
    --pattern-mid: #e3ecdd;
    --matcha: #4f8a3c;
    --ink: #222222;
    --badge: #2f6b2a;
  }
  * { box-sizing: border-box; margin: 0; padding: 0; }
  html, body { width: 1200px; height: 234px; overflow: hidden; background: var(--paper); }
  .label {
    position: relative;
    width: 1200px;
    height: 234px;
    font-family: "Fredoka", sans-serif;
    color: var(--ink);
    overflow: hidden;
  }
  .label__pattern {
    position: absolute;
    inset: 0;
    background: linear-gradient(90deg, var(--pattern-light), var(--pattern-mid) 50%, var(--pattern-light));
  }
  .front-panel {
    position: absolute;
    left: 478px;
    top: 7px;
    width: 244px;
    height: 220px;
    background: var(--paper);
    border: 2px solid var(--matcha);
    display: flex;
    flex-direction: column;
    align-items: center;
    text-align: center;
  }
  .front-panel__brand {
    margin-top: 66px;
    display: flex;
    align-items: center;
    gap: 8px;
    font-family: "Alfa Slab One", serif;
    font-size: 27px;
    color: var(--ink);
  }
  .front-panel__dot {
    width: 12px;
    height: 12px;
    border-radius: 50%;
    background: var(--matcha);
  }
  .front-panel__desc {
    margin-top: 12px;
    font-size: 10.5px;
    font-weight: 600;
    letter-spacing: 0.5px;
    line-height: 1.35;
    text-transform: uppercase;
  }
  .front-panel__weight {
    margin-top: 14px;
    font-size: 9.5px;
    font-weight: 500;
    font-variant: small-caps;
  }
  .distribution {
    position: absolute;
    left: 84px;
    top: 123px;
    font-size: 9px;
    font-weight: 500;
    line-height: 1.45;
    font-variant: small-caps;
    background: var(--paper);
    padding: 2px 4px;
  }
  .info {
    position: absolute;
    left: 820px;
    top: 40px;
    width: 300px;
    font-size: 8.5px;
    font-weight: 500;
    line-height: 1.45;
    font-variant: small-caps;
  }
  .info__heading { font-weight: 700; text-transform: uppercase; font-size: 8.5px; }
  .info__block { background: var(--paper); padding: 1px 4px; display: inline-block; margin-bottom: 6px; }
  .info__list { list-style: none; padding-left: 6px; }
  .info__list li::before { content: "• "; }
  .storage {
    position: absolute;
    left: 994px;
    top: 150px;
    display: flex;
    align-items: center;
    gap: 8px;
  }
  .storage__badge {
    width: 30px;
    height: 30px;
    border-radius: 50%;
    background: var(--badge);
  }
  .storage__text {
    font-size: 8px;
    font-weight: 700;
    text-transform: uppercase;
    line-height: 1.3;
    background: var(--paper);
    padding: 1px 3px;
  }
</style>
</head>
<body>
  <div class="label">
    <div class="label__pattern" role="img" aria-label="Faint repeating pattern of matcha tools, tea leaves and teacups"></div>

    <div class="distribution">
      Distributed by Lumo Brew | Maple Falls, VT<br>
      Certified Organic by GreenLeaf<br>
      Product of Japan
    </div>

    <section class="front-panel">
      <div class="front-panel__brand">
        <span class="front-panel__dot"></span>
        <span>Lumo Brew</span>
      </div>
      <p class="front-panel__desc">Premium Organic<br>Ceremonial Matcha</p>
      <p class="front-panel__weight">Net Wt. 30g</p>
    </section>

    <div class="info">
      <div class="info__block">
        <p class="info__heading">Ingredients</p>
        <p>Premium Organic Japanese Matcha Green Tea</p>
      </div><br>
      <div class="info__block">
        <p class="info__heading">Instructions</p>
        <ul class="info__list">
          <li>1 tsp of Matcha</li>
          <li>3oz of water (175-185 degrees F)</li>
          <li>Whisk in a W formation until frothy</li>
          <li>Sweeten to taste</li>
        </ul>
      </div>
    </div>

    <div class="storage">
      <div class="storage__badge" aria-hidden="true"></div>
      <p class="storage__text">Keep refrigerated<br>for quality</p>
    </div>
  </div>
</body>
</html>
```